Bref créative
Business Card for financial advisor
RVT Service Providers
Simple
Irina Lebedinskaya
Director
42 Marlow Yard
London
SW9 3QT
irina.lebedinskaya@rvtsupport.example

```html
<!DOCTYPE html>
<html lang="en">
<head>
<meta charset="utf-8">
<title>RVT Service Providers — Business Card</title>
<link rel="stylesheet" href="https://fonts.googleapis.com/css2?family=Open+Sans:wght@400;600;700&display=swap">
<style>
  :root {
    --bg: #e9eaec;
    --card: #ffffff;
    --brand-red: #d3222a;
    --ink: #3a3a3c;
    --shadow-band: #4a4a4d;
    --on-red: #ffffff;
  }
  * { margin: 0; padding: 0; box-sizing: border-box; }
  html, body {
    width: 1200px;
    height: 1009px;
    overflow: hidden;
    background: var(--bg);
  }
  .sheet {
    width: 1200px;
    height: 1009px;
    display: flex;
    flex-direction: column;
    align-items: center;
    justify-content: center;
    gap: 34px;
  }
  .card {
    position: relative;
    width: 820px;
    height: 468px;
    background: var(--card);
    border-radius: 22px;
    overflow: hidden;
    box-shadow: 0 10px 28px rgba(0,0,0,0.12);
  }

  /* Company name */
  .company {
    display: flex;
    align-items: center;
    font-family: "Open Sans", sans-serif;
    font-weight: 700;
    color: var(--ink);
    line-height: 1;
    white-space: nowrap;
  }
  .company__mark {
    flex: none;
    background: var(--brand-red);
  }

  .card--logo .company {
    position: absolute;
    left: 0; right: 0;
    top: 50%;
    transform: translateY(-50%);
    justify-content: center;
    gap: 22px;
    font-size: 60px;
  }
  .card--logo .company__mark { width: 44px; height: 44px; }

  /* Contact side */
  .card--contact .wave { position: absolute; inset: 0; }
  .card--contact .company {
    position: absolute;
    left: 44px;
    top: 56px;
    gap: 12px;
    font-size: 23px;
  }
  .card--contact .company__mark { width: 18px; height: 18px; }

  .contact {
    position: absolute;
    left: 430px;
    top: 180px;
    color: var(--on-red);
    font-family: "Open Sans", sans-serif;
  }
  .contact__name { font-size: 26px; font-weight: 600; }
  .contact__role { font-size: 17px; margin-top: 2px; font-style: italic; }
  .contact__details { list-style: none; margin-top: 26px; font-size: 15px; line-height: 1.55; }
  .contact__details li { display: flex; align-items: center; gap: 10px; }
  .contact__details .spacer { width: 14px; flex: none; }
  .contact__details svg { width: 14px; height: 14px; flex: none; fill: var(--on-red); }
</style>
</head>
<body>
<main class="sheet">

  <section class="card card--logo" aria-label="Business card, front side">
    <p class="company"><span class="company__mark" aria-hidden="true"></span>RVT Service Providers</p>
  </section>

  <section class="card card--contact" aria-label="Business card, contact side">
    <svg class="wave" viewBox="0 0 820 468" preserveAspectRatio="none" aria-hidden="true">
      <path fill="var(--shadow-band)" d="M400 0 L820 0 L820 468 L0 468 L0 388 C150 372 245 320 278 215 C312 105 330 22 400 0 Z"/>
      <path fill="var(--brand-red)" d="M440 0 L820 0 L820 468 L0 468 L0 412 C165 398 270 345 305 235 C342 118 365 24 440 0 Z"/>
    </svg>

    <p class="company"><span class="company__mark" aria-hidden="true"></span>RVT Service Providers</p>

    <div class="contact">
      <p class="contact__name">Irina Lebedinskaya</p>
      <p class="contact__role">Director</p>
      <ul class="contact__details">
        <li><span class="spacer"></span>42 Marlow Yard, London</li>
        <li><span class="spacer"></span>SW9 3QT</li>
        <li>
          <svg viewBox="0 0 24 24" aria-hidden="true"><path d="M6.6 10.8a15.1 15.1 0 0 0 6.6 6.6l2.2-2.2c.3-.3.7-.4 1-.2 1.1.4 2.3.6 3.6.6.6 0 1 .4 1 1V20c0 .6-.4 1-1 1C10.6 21 3 13.4 3 4c0-.6.4-1 1-1h3.5c.6 0 1 .4 1 1 0 1.3.2 2.5.6 3.6.1.3 0 .7-.2 1l-2.3 2.2z"/></svg>
          +44 (0) 200 000 1234
        </li>
        <li>
          <svg viewBox="0 0 24 24" aria-hidden="true"><path d="M7 2h10a2 2 0 0 1 2 2v16a2 2 0 0 1-2 2H7a2 2 0 0 1-2-2V4a2 2 0 0 1 2-2zm0 3v13h10V5H7z"/></svg>
          +44 (0) 700 000 5678
        </li>
        <li>
          <svg viewBox="0 0 24 24" aria-hidden="true"><path d="M3 5h18v14H3V5zm2 2v.5l7 4.5 7-4.5V7H5zm14 2.9-7 4.5-7-4.5V17h14V9.9z"/></svg>
          irina.lebedinskaya@rvtsupport.example
        </li>
      </ul>
    </div>
  </section>

</main>
</body>
</html>
```